Newsletter-Design für eine Yogalehrerin
Zielgruppe
Ich bin Yogalehrerin.
Meine Zielgruppe sind hauptsächlich Erwachsene (Frauen und Männer) welche Privatyoga Online praktizieren.
Aufgabenstellung
Gerne auch, aber nicht nur das Layout und die Texte von der Webseite www.atemkreis-nord.ch verwenden.
Es sollte ein ansprechender Newsletter für Online Privatyoga gestaltet werden um mehr Teilnehmer zu gewinnen.

```html
<!DOCTYPE html>
<html lang="de">
<head>
<meta charset="utf-8">
<title>Atemkreis – Newsletter Online Privatyoga</title>
<link rel="stylesheet" href="https://fonts.googleapis.com/css2?family=Caveat:wght@500&family=Open+Sans:wdth,wght@75..100,300..700&display=swap">
<style>
:root{
  --page:#ffffff;
  --sand:#ece3db;
  --card:#f4f0ea;
  --accent:#e85a35;
  --accent-soft:#f0a584;
  --ink:#3a3330;
  --logo:#8a7f78;
  --lavender:#c3aae6;
  --salmon:#f39d8c;
  --sky:#7ec8e3;
  --teal:#5fa89c;
  --photo-warm:#d8c7b8;
  --photo-light:#e9e4de;
}
*{margin:0;padding:0;box-sizing:border-box}
html,body{width:741px;height:1200px;overflow:hidden;background:var(--page)}
body{position:relative;font-family:"Open Sans",Arial,sans-serif;color:var(--ink)}

.frame{position:absolute;overflow:hidden;box-shadow:0 2px 10px rgba(0,0,0,.12)}
.frame--desktop{left:75px;top:38px;width:256px;height:1133px}
.frame--mobile{left:406px;top:392px;width:221px;height:454px;border-radius:14px 14px 0 0;box-shadow:0 2px 8px rgba(0,0,0,.10)}

.newsletter{position:absolute;left:0;top:0;width:518px;height:2293px;background:var(--page);transform-origin:0 0}
.frame--desktop .newsletter{transform:scale(.494)}
.frame--mobile .newsletter{transform:scale(.427)}

.abs{position:absolute}
.band{position:absolute;left:0;width:518px;background:var(--sand)}
.photo{position:absolute}

.headline{font-stretch:75%;font-weight:300;color:var(--accent);font-size:28px;line-height:27px}
.copy{font-size:12.5px;line-height:17.6px;font-weight:400;color:var(--ink)}
.btn{position:absolute;background:var(--accent);color:#fff;font-weight:700;display:flex;align-items:center;justify-content:center;font-size:10px;letter-spacing:.2px;text-transform:uppercase}
.script{font-family:"Caveat",cursive}
.center{text-align:center}

.logo{position:absolute;left:0;width:518px;top:30px;text-align:center}
.logo__dot{display:block;width:38px;height:38px;border-radius:50%;border:2px solid var(--accent-soft);margin:0 auto 14px}
.logo__name{font-size:22px;letter-spacing:2px;color:var(--logo);font-weight:400}

.laptop__screen{left:107px;top:137px;width:308px;height:206px;border:5px solid #d9dde2;border-radius:6px 6px 0 0;background:linear-gradient(120deg,#cfc3b5,#f3eee7 45%,#b7b0b8)}
.laptop__base{left:71px;top:343px;width:382px;height:10px;background:linear-gradient(#e2e5e9,#b9bec5);border-radius:0 0 40px 40px}

.card{position:absolute;top:615px;width:194px;height:238px;background:var(--card)}
.card__photo{position:absolute;left:0;top:0;width:194px;height:93px}
.card__title{position:absolute;left:0;top:98px;width:194px;text-align:center;font-size:25px;line-height:26px}
.card__text{position:absolute;left:10px;top:155px;width:174px;text-align:center}

.tile{position:absolute;top:1619px;width:102px;height:212px}
.tile__photo{position:absolute;left:0;top:0;width:102px;height:164px}
.tile__label{position:absolute;left:0;top:164px;width:102px;height:48px;padding:20px 0 0 7px;color:#fff;font-size:8.5px;line-height:10px;font-stretch:75%;text-transform:uppercase}

.social{position:absolute;top:2165px;width:30px;height:30px;border-radius:50%;background:#f2d6c9}
.footer{position:absolute;left:0;width:518px;text-align:center;font-size:8px;line-height:9.5px;color:#555}
.footer a{color:var(--accent);font-weight:700;text-decoration:underline}
</style>
</head>
<body>

<!-- Desktop newsletter -->
<div class="frame frame--desktop">
<div class="newsletter">
  <div class="band" style="top:0;height:478px"></div>
  <div class="logo"><span class="logo__dot"></span><span class="logo__name">ATEMKREIS</span></div>
  <div class="abs photo laptop__screen" role="img" aria-label="Laptop mit Foto einer meditierenden Frau im hellen Wohnzimmer"></div>
  <div class="abs laptop__base"></div>
  <div class="abs script center" style="left:0;top:368px;width:518px;font-size:28px;color:var(--accent-soft)">Entdecke jetzt</div>
  <div class="abs headline center" style="left:0;top:398px;width:518px;font-size:46px;line-height:48px">Online Privatyoga</div>
  <div class="btn" style="left:171px;top:460px;width:179px;height:31px;font-size:14px;text-transform:none">Jetzt mehr erfahren</div>

  <p class="abs copy center" style="left:84px;top:516px;width:350px">Privatyoga bietet dir – Eins zu Eins Übungen. Ich zeige dir in Privatstunden wie du bestmöglichst, nicht durch Symptombe­handlung, sondern durch Mensch in deiner Ganzheit zu besse­rem Umgang und Wohlbefinden zurückfindest …</p>

  <div class="card" style="left:57px">
    <div class="card__photo" role="img" aria-label="Foto: Yogalehrerin korrigiert die Haltung einer Schülerin" style="background:linear-gradient(90deg,#d9b9a0,#f1e9e2 50%,#3b3a40)"></div>
    <div class="card__title headline">Mehr über<br>Online Privatyoga</div>
    <p class="card__text copy">Du lernst Techniken, die du selbstständig anwenden und für dich umsetzen kannst.</p>
  </div>
  <div class="btn" style="left:85px;top:841px;width:138px;height:27px">Mehr erfahren</div>

  <div class="card" style="left:270px">
    <div class="card__photo" role="img" aria-label="Foto: Mann übt Liegestütz auf einer Yogamatte zu Hause" style="background:linear-gradient(#eeeae5,#c9c2bb 60%,#d39d72)"></div>
    <div class="card__title headline">Trainiere wann und<br>wo du willst</div>
    <p class="card__text copy">Du übst und entspannst dich in geschützter Atmo­sphäre, z.B bei dir zu Hause.</p>
  </div>
  <div class="btn" style="left:297px;top:841px;width:138px;height:27px">Stunden buchen</div>

  <div class="band" style="top:928px;height:288px"></div>
  <div class="photo" role="img" aria-label="Foto: Mann meditiert im Schneidersitz mit gefalteten Händen" style="left:0;top:960px;width:194px;height:220px;background:linear-gradient(160deg,#e6ddd3,#8a4a40 55%,#3c3733)"></div>
  <div class="abs headline" style="left:252px;top:970px">Yoga fördert<br>die Gelassenheit</div>
  <p class="abs copy" style="left:252px;top:1030px;width:205px">Yoga ist der Schlüssel zu einem glücklichen Leben. Es liefert Techni­ken, die Körper, Geist und Atem mit­einander verbinden und uns ins innere Gleichgewicht bringen.</p>
  <div class="btn" style="left:252px;top:1134px;width:154px;height:27px">Mehr erfahren</div>

  <div class="abs headline" style="left:0;top:1292px;width:270px;text-align:right">YOGA ist für jeden</div>
  <p class="abs copy" style="left:70px;top:1324px;width:200px;text-align:right">Du musst weder sportlich oder gelenkig sein, auch das Alter spielt keine Rolle. Jeder kann jederzeit mit der Praxis des Yoga beginnen.</p>
  <div class="btn" style="left:135px;top:1414px;width:135px;height:27px">Jetzt buchen</div>
  <div class="photo" role="img" aria-label="Foto: Mutter und Kind üben gemeinsam den herabschauenden Hund" style="left:324px;top:1254px;width:194px;height:220px;background:linear-gradient(135deg,#eeeeec,#cfd2d6 50%,#b49a7a)"></div>

  <div class="band" style="top:1532px;height:251px"></div>
  <div class="abs headline center" style="left:0;top:1566px;width:518px">Weitere Kurs Angebote</div>
  <div class="tile" style="left:57px">
    <div class="tile__photo" role="img" aria-label="Foto: Mann meditiert" style="background:linear-gradient(#8c7a6c,#3b3836)"></div>
    <div class="tile__label" style="background:var(--lavender)">Yoga für<br>Erwachsene</div>
  </div>
  <div class="tile" style="left:159px">
    <div class="tile__photo" role="img" aria-label="Foto: Mädchen macht Yoga" style="background:linear-gradient(#f2efea,#b5a6c8)"></div>
    <div class="tile__label" style="background:var(--salmon)">Yoga für<br>Kinder</div>
  </div>
  <div class="tile" style="left:261px">
    <div class="tile__photo" role="img" aria-label="Foto: Babybauch einer Schwangeren" style="background:linear-gradient(90deg,#f4f1ee,#e7c3ac)"></div>
    <div class="tile__label" style="background:var(--sky)">Yoga für<br>Schwangere</div>
  </div>
  <div class="tile" style="left:363px">
    <div class="tile__photo" role="img" aria-label="Foto: ältere Frau meditiert" style="background:linear-gradient(#dfe4e6,#3d7aa2)"></div>
    <div class="tile__label" style="background:var(--teal)">Yoga für<br>Senioren</div>
  </div>

  <div class="band" style="top:1923px;height:205px"></div>
  <div class="photo" role="img" aria-label="Porträtfoto der Yogalehrerin" style="left:208px;top:1870px;width:102px;height:102px;border-radius:50%;background:radial-gradient(circle,#e9c6ad,#a77a52)"></div>
  <div class="abs headline center" style="left:0;top:1986px;width:518px">Kontaktiere mich und buche<br>deinen Kurs</div>
  <p class="abs copy center" style="left:95px;top:2048px;width:328px">Ich bin zertifizierte Yogalehrerin und habe mich zusätzlich für Yogatherapie und Yoga für Kinder weitergebildet. Seit über elf Jahren praktiziere ich hauptsächlich Hatha Yoga.</p>
  <div class="abs script center" style="left:0;top:2102px;width:518px;font-size:32px;color:var(--accent)">Lea Brunner</div>

  <div class="social" style="left:224px" aria-label="Social Media"></div>
  <div class="social" style="left:261px" aria-label="Messenger"></div>
  <p class="footer" style="top:2208px">www.atemkreis-nord.ch</p>
  <p class="footer" style="top:2224px">Lorem ipsum dolor sit amet, consectetuer adipiscing elit aenean: <a>Unsubscribe here</a><br>commodo ligula eget dolor. Aenean massa. Cum sociis natoque penatibus et ma</p>
</div>
</div>

<!-- Mobile newsletter -->
<div class="frame frame--mobile">
<div class="newsletter">
  <div class="band" style="top:0;height:478px"></div>
  <div class="logo"><span class="logo__dot"></span><span class="logo__name">ATEMKREIS</span></div>
  <div class="abs photo laptop__screen" role="img" aria-label="Laptop mit Foto einer meditierenden Frau im hellen Wohnzimmer"></div>
  <div class="abs laptop__base"></div>
  <div class="abs script center" style="left:0;top:368px;width:518px;font-size:28px;color:var(--accent-soft)">Entdecke jetzt</div>
  <div class="abs headline center" style="left:0;top:398px;width:518px;font-size:46px;line-height:48px">Online Privatyoga</div>
  <div class="btn" style="left:171px;top:460px;width:179px;height:31px;font-size:14px;text-transform:none">Jetzt mehr erfahren</div>

  <p class="abs copy center" style="left:84px;top:516px;width:350px">Privatyoga bietet dir – Eins zu Eins Übungen. Ich zeige dir in Privatstunden wie du bestmöglichst, nicht durch Symptombe­handlung, sondern durch Mensch in deiner Ganzheit zu besse­rem Umgang und Wohlbefinden zurückfindest …</p>

  <div class="card" style="left:57px">
    <div class="card__photo" role="img" aria-label="Foto: Yogalehrerin korrigiert die Haltung einer Schülerin" style="background:linear-gradient(90deg,#d9b9a0,#f1e9e2 50%,#3b3a40)"></div>
    <div class="card__title headline">Mehr über<br>Online Privatyoga</div>
    <p class="card__text copy">Du lernst Techniken, die du selbstständig anwenden und für dich umsetzen kannst.</p>
  </div>
  <div class="btn" style="left:85px;top:841px;width:138px;height:27px">Mehr erfahren</div>

  <div class="card" style="left:270px">
    <div class="card__photo" role="img" aria-label="Foto: Mann übt Liegestütz auf einer Yogamatte zu Hause" style="background:linear-gradient(#eeeae5,#c9c2bb 60%,#d39d72)"></div>
    <div class="card__title headline">Trainiere wann und<br>wo du willst</div>
    <p class="card__text copy">Du übst und entspannst dich in geschützter Atmo­sphäre, z.B bei dir zu Hause.</p>
  </div>
  <div class="btn" style="left:297px;top:841px;width:138px;height:27px">Stunden buchen</div>

  <div class="band" style="top:928px;height:288px"></div>
  <div class="photo" role="img" aria-label="Foto: Mann meditiert im Schneidersitz mit gefalteten Händen" style="left:0;top:960px;width:194px;height:220px;background:linear-gradient(160deg,#e6ddd3,#8a4a40 55%,#3c3733)"></div>
  <div class="abs headline" style="left:252px;top:970px">Yoga fördert<br>die Gelassenheit</div>
  <p class="abs copy" style="left:252px;top:1030px;width:205px">Yoga ist der Schlüssel zu einem glücklichen Leben. Es liefert Techni­ken, die Körper, Geist und Atem mit­einander verbinden und uns ins innere Gleichgewicht bringen.</p>
</div>
</div>

</body>
</html>
```